NEW YORK Plumbing/utility company 10 year anniversary business card

Looking For simple back and front business card would like to include a few things in description
We offer 24/7 emergency service
residential
commercial
industrial
municipal
services offered
Plumbing
hydro excavation
hydro jetting
Well pumps
Sewer pumps
water mains
sewer mains

```html
<!DOCTYPE html>
<html lang="en">
<head>
<meta charset="utf-8">
<title>Ridgeline Water &amp; Sewer – Business Card</title>
<link href="https://fonts.googleapis.com/css2?family=Montserrat:wght@400;600;700;800&display=swap" rel="stylesheet">
<style>
  :root {
    --backdrop: #2a2a2a;
    --paper: #ffffff;
    --brand-blue: #0a62a6;
    --brand-red: #f80000;
    --accent-sky: #11a9ea;
    --ink-white: #ffffff;
  }
  * { box-sizing: border-box; margin: 0; padding: 0; }
  html, body {
    width: 1200px; height: 1024px; overflow: hidden;
    background: var(--backdrop);
    font-family: "Montserrat", sans-serif;
  }
  .sheet {
    width: 1200px; height: 1024px;
    display: flex; flex-direction: column; align-items: center; justify-content: center;
    gap: 20px;
  }
  .card {
    position: relative;
    width: 840px; height: 480px;
    background: var(--paper);
    overflow: hidden;
    box-shadow: 0 10px 30px rgba(0,0,0,.5);
  }

  /* brand name lockup */
  .brand {
    display: flex; align-items: center; justify-content: center; gap: 18px;
    color: var(--brand-blue);
    font-weight: 800;
    text-transform: uppercase;
    white-space: nowrap;
  }
  .brand__dot {
    width: 46px; height: 46px; border-radius: 50%;
    background: var(--brand-blue);
    flex: none;
  }

  /* front */
  .front__brand {
    position: absolute; left: 0; right: 0; top: 120px;
    font-size: 42px; letter-spacing: 3px;
  }
  .front__contact-band {
    position: absolute; left: 0; right: 0; bottom: 0; height: 135px;
    background: var(--brand-red);
    display: flex; align-items: center; justify-content: center; gap: 48px;
    color: var(--ink-white);
    font-size: 30px; font-weight: 600;
  }
  .contact-item { display: flex; align-items: center; gap: 12px; }
  .contact-item svg { width: 36px; height: 36px; flex: none; }

  /* back */
  .back__brand {
    position: absolute; left: 0; right: 0; top: 50px;
    font-size: 38px; letter-spacing: 3px;
  }
  .back__market-band {
    position: absolute; left: 0; right: 0; top: 150px; height: 136px;
    background: var(--brand-blue);
    color: var(--ink-white);
    text-align: center;
    padding-top: 22px;
  }
  .back__headline {
    font-size: 32px; font-weight: 800; letter-spacing: 1px; line-height: 1.2;
  }
  .back__rule {
    position: relative; width: 640px; height: 3px; margin: 12px auto 14px;
    background: linear-gradient(90deg, transparent, var(--accent-sky) 20%, var(--accent-sky) 80%, transparent);
  }
  .back__rule::after {
    content: ""; position: absolute; left: 50%; top: 50%;
    width: 11px; height: 11px; border-radius: 50%;
    background: var(--accent-sky); transform: translate(-50%, -50%);
  }
  .back__markets {
    display: flex; justify-content: center; gap: 18px;
    font-size: 20px; font-weight: 800; line-height: 1.2;
  }
  .back__markets .sep { color: var(--accent-sky); font-weight: 400; }

  .back__services {
    position: absolute; left: 0; right: 0; top: 298px;
    text-align: center;
  }
  .services__title {
    display: flex; align-items: center; justify-content: center; gap: 16px;
    color: var(--accent-sky); font-size: 26px; font-weight: 800; line-height: 1.2;
  }
  .services__title::before, .services__title::after {
    content: ""; width: 230px; height: 2px; background: var(--accent-sky);
  }
  .services__list {
    margin-top: 6px;
    color: var(--brand-red); font-size: 21px; font-weight: 400; line-height: 1.35;
  }
  .services__list .bullet { color: var(--accent-sky); margin: 0 6px; }
  .back__divider {
    position: absolute; left: 0; right: 0; top: 400px; height: 2px;
    background: var(--accent-sky);
  }
  .back__footer-band {
    position: absolute; left: 0; right: 0; bottom: 0; height: 68px;
    background: var(--brand-red);
  }
</style>
</head>
<body>
<main class="sheet">

  <section class="card card--front" aria-label="Business card front">
    <div class="brand front__brand">
      <span class="brand__dot"></span>
      <span class="brand__name">Ridgeline Water &amp; Sewer</span>
    </div>
    <div class="front__contact-band">
      <div class="contact-item">
        <svg viewBox="0 0 36 36" aria-hidden="true">
          <rect x="1" y="1" width="34" height="34" rx="9" fill="#fff"/>
          <path d="M12 9c1-1 2.5-1 3 .5l1.5 3.5c.4 1-.2 1.8-1 2.4l-1 .8c1 2.4 3 4.4 5.3 5.4l.8-1c.6-.8 1.5-1.3 2.4-1l3.5 1.5c1.4.5 1.5 2 .5 3l-1.7 1.7c-1.3 1.3-3.4 1.5-5.3.5-4.3-2.2-7.6-5.500-9.8-9.8-1-1.9-.8-4 .5-5.3z" fill="var(--brand-blue)"/>
        </svg>
        <span>555-014-2290</span>
      </div>
      <div class="contact-item">
        <svg viewBox="0 0 36 36" aria-hidden="true">
          <rect x="1" y="1" width="34" height="34" rx="9" fill="#fff"/>
          <rect x="8" y="11" width="20" height="14" rx="2" fill="var(--brand-blue)"/>
          <path d="M9 12l9 7 9-7" stroke="#fff" stroke-width="1.8" fill="none"/>
        </svg>
        <span>info@ridgelinews.com</span>
      </div>
    </div>
  </section>

  <section class="card card--back" aria-label="Business card back">
    <div class="brand back__brand">
      <span class="brand__dot"></span>
      <span class="brand__name">Ridgeline Water &amp; Sewer</span>
    </div>
    <div class="back__market-band">
      <p class="back__headline">WE OFFER 24/7 EMERGENCY SERVICE</p>
      <div class="back__rule"></div>
      <p class="back__markets">
        <span>RESIDENTIAL</span><span class="sep">|</span>
        <span>COMMERCIAL</span><span class="sep">|</span>
        <span>INDUSTRIAL</span><span class="sep">|</span>
        <span>MUNICIPAL</span>
      </p>
    </div>
    <div class="back__services">
      <h2 class="services__title">SERVICES OFFERED</h2>
      <p class="services__list">
        Plumbing<span class="bullet">•</span>Hydro Excavation<span class="bullet">•</span>Hydro Jetting<span class="bullet">•</span>Well Pumps<br>
        Sewer Pumps<span class="bullet">•</span>Water Mains<span class="bullet">•</span>Sewer Mains
      </p>
    </div>
    <div class="back__divider"></div>
    <div class="back__footer-band"></div>
  </section>

</main>
</body>
</html>
```